Corporate Travel Technology Company needs new Business Card design

We need a new business card design to reflect our re-branded company. Our company is called vendaXo (pronounced eureka) and we provide Business Intelligence and mobile travel management solutions for the corporate travel industry. Our multinational customers use our solutions to manage large travel budgets and frequent travellers, as well as to save money and reduce risk. We'd like to see designs that use the blue and green palette as well as our corporate logo (attached below). The design should communicate innovation, insight, forward thinking, contemporary, trusted.

Target Market(s)

Large multinational corporates and Travel Agencies.

Industry/Entity Type

Business

Contact Information for Business Card

Marguerite Tallis
Chief Executive
vendaXo
Phone number - +61 (0)2 8147 3092
Email address - marguerite.tallis@vendaxo.example
Mobile number - +61 (0)455 206 718
www.vendaxo.example

Font styles to use
Other font styles liked:
• Please use font as close to corporate logo as possible

Colors
0255a3
0393ce
00a990
33b8a4
33a6d7
3176b5

Requirements
Must have
• Please include the words;
• Mobile Travel Management
• Accelerating Travel Business Insights
• Use corporate logo - although icon can be stylised if needed

```html
<!DOCTYPE html>
<html lang="en">
<head>
<meta charset="utf-8">
<title>vendaXo Business Card</title>
<link rel="stylesheet" href="https://fonts.googleapis.com/css2?family=Open+Sans:wght@400&family=Roboto:wght@400;700&display=swap">
<style>
  :root {
    --page: #ffffff;
    --mat: #d1d3d4;
    --brand-deep: #0b55a3;
    --brand-glow: #0693d0;
    --ink: #3a3a3a;
    --white: #ffffff;
  }
  * { box-sizing: border-box; margin: 0; padding: 0; }
  html, body { width: 1200px; height: 440px; overflow: hidden; background: var(--page); }
  .sheet { position: relative; width: 1200px; height: 440px; }
  .mat { position: absolute; left: 14px; top: 40px; width: 1176px; height: 360px; background: var(--mat); }

  .blue-field {
    position: absolute;
    background: radial-gradient(circle at 50% 45%, var(--brand-glow) 0%, #1570b8 38%, var(--brand-deep) 80%);
    color: var(--white);
    display: flex; flex-direction: column; align-items: center;
  }
  .card-front { left: 23px; top: 46px; width: 560px; height: 336px; }
  .card-back-brand { left: 898px; top: 46px; width: 281px; height: 336px; justify-content: center; }

  .wordmark {
    font-family: 'Roboto', sans-serif; font-weight: 400;
    color: var(--white); display: flex; align-items: center; gap: 10px; line-height: 1;
  }
  .wordmark .dot { width: 22px; height: 22px; border-radius: 50%; background: var(--white); }
  .card-front .wordmark { margin-top: 158px; font-size: 58px; }
  .card-back-brand .wordmark { font-size: 50px; margin-top: -18px; }
  .card-back-brand .wordmark .dot { width: 18px; height: 18px; }

  .taglines {
    margin-top: auto; margin-bottom: 22px;
    font-family: 'Roboto', sans-serif; font-size: 16px; line-height: 22px; text-align: center;
  }

  .card-back-info {
    position: absolute; left: 621px; top: 46px; width: 277px; height: 336px;
    background: var(--white); padding: 28px 8px 0 20px; overflow: hidden;
  }
  .name {
    font-family: 'Roboto', sans-serif; font-weight: 700; font-size: 24px; line-height: 1;
    color: var(--ink); text-transform: uppercase; letter-spacing: -0.3px; white-space: nowrap;
  }
  .name .surname { color: var(--brand-deep); }
  .role { font-family: 'Roboto', sans-serif; font-size: 20px; color: var(--ink); margin-top: 7px; }

  .contacts { list-style: none; margin-top: 52px; }
  .contacts li {
    display: flex; align-items: center; gap: 14px;
    font-family: 'Open Sans', sans-serif; font-size: 14px; line-height: 17px; color: var(--ink);
    white-space: nowrap;
  }
  .contacts li + li { margin-top: 26px; }
  .contacts svg { width: 28px; height: 28px; flex: none; }
  .icon-solid { fill: var(--brand-deep); }
  .icon-line { fill: none; stroke: var(--brand-deep); stroke-width: 2.4; }
  .contact-email { font-size: 11.5px; letter-spacing: -0.1px; }
</style>
</head>
<body>
<div class="sheet">
  <div class="mat"></div>

  <section class="blue-field card-front">
    <div class="wordmark"><span class="dot"></span>vendaXo</div>
    <p class="taglines">Mobile Travel Management<br>Accelerating Travel Business Insights</p>
  </section>

  <section class="card-back-info">
    <h1 class="name">Marguerite<span class="surname">Tallis</span></h1>
    <p class="role">Chief Executive</p>
    <ul class="contacts">
      <li>
        <svg class="icon-solid" viewBox="0 0 32 32" aria-hidden="true"><path d="M8 3c1-1 2.5-1 3.3.2l3 4.4c.7 1 .5 2.3-.4 3.1l-2 1.8c1.3 3 3.6 5.6 6.6 7.2l1.9-2c.8-.9 2.2-1 3.1-.3l4.3 3.1c1.1.8 1.2 2.3.2 3.3l-2.3 2.4c-1.2 1.2-3 1.6-4.6 1C12.7 25 6.5 18.6 4.3 10.3 3.9 8.7 4.4 7 5.6 5.8z"/></svg>
        <span>+61 (0)2 8147 3092<br>+61 (0)455 206 718</span>
      </li>
      <li>
        <svg class="icon-solid" viewBox="0 0 32 32" aria-hidden="true"><path d="M2 7h28v18H2z"/><path d="M4 10l12 8 12-8v1.5L16 19.5 4 11.5z" fill="#fff"/></svg>
        <span class="contact-email">marguerite.tallis@vendaxo.example</span>
      </li>
      <li>
        <svg class="icon-line" viewBox="0 0 32 32" aria-hidden="true"><circle cx="16" cy="16" r="13"/><ellipse cx="16" cy="16" rx="6" ry="13"/><path d="M3 16h26M5.5 9h21M5.5 23h21"/></svg>
        <span>www.vendaxo.example</span>
      </li>
    </ul>
  </section>

  <section class="blue-field card-back-brand">
    <div class="wordmark"><span class="dot"></span>vendaXo</div>
  </section>
</div>
</body>
</html>
```